Brantwell Group needs a business card design

We need a new business card design using the logo recently selected in a logo competition on Pixel Forum. Our business is a consultancy specializing in aviation and energy and the winning business card design will promote an image of precision and professionalism with creativity.

Please use the logo with the name on the front of the card and use a complementary font. Make the back white with either the light grey or dark grey logo.

Target Market(s)

Senior finance and legal leaders at aviation and energy companies

Industry/Entity Type

Management Consulting

Contact Information for Business Card

Peter Haldane
President
Brantwell Group

www.brantwellgroup.example

(555) 304-6198
ph@brantwellgroup.example

Requirements
Must have
• Professional font that goes well with the logo font

```html
<!DOCTYPE html>
<html lang="en">
<head>
<meta charset="utf-8">
<title>Brantwell Group – Business Card</title>
<link rel="stylesheet" href="https://fonts.googleapis.com/css2?family=Raleway:wght@300;400&display=swap">
<style>
  :root {
    --backdrop: #e7e5e1;
    --card-white: #ffffff;
    --brand-blue: #2d5a8c;
    --panel-top: #1f4f86;
    --panel-bottom: #123763;
    --panel-text: #e6eef8;
    --brand-grey: #b9bdc3;
    --web-grey: #6f747b;
    --shadow: rgba(40, 35, 30, 0.28);
  }
  * { box-sizing: border-box; margin: 0; padding: 0; }
  html, body {
    width: 1200px; height: 843px; overflow: hidden;
    background: var(--backdrop);
    font-family: "Raleway", sans-serif;
  }
  .stage { position: relative; width: 1200px; height: 843px; }

  .card {
    position: absolute;
    width: 560px; height: 320px;
    background: var(--card-white);
    border-radius: 3px;
    box-shadow: 0 14px 32px var(--shadow);
    overflow: hidden;
  }
  .card--back { left: 120px; top: 90px; }
  .card--front { left: 520px; top: 433px; display: flex; }

  /* Back side */
  .back-name {
    position: absolute; left: 0; right: 0; top: 112px;
    text-align: center;
    font-weight: 300; font-size: 34px; letter-spacing: 8px;
    color: var(--brand-grey); text-transform: uppercase;
  }
  .back-web {
    position: absolute; left: 0; right: 0; bottom: 36px;
    text-align: center;
    font-weight: 400; font-size: 13px; letter-spacing: 5px;
    color: var(--web-grey);
  }

  /* Front side */
  .front-brand {
    width: 54%;
    display: flex; align-items: center; justify-content: center;
    gap: 12px;
  }
  .brand-mark { width: 14px; height: 14px; background: var(--brand-blue); }
  .brand-name {
    font-weight: 300; font-size: 25px; letter-spacing: 4px;
    color: var(--brand-blue); text-transform: uppercase;
    line-height: 1.25;
  }
  .front-details {
    width: 46%;
    background: linear-gradient(160deg, var(--panel-top), var(--panel-bottom));
    color: var(--panel-text);
    padding: 30px 26px 0 22px;
    font-weight: 300;
  }
  .person-name { font-size: 17px; letter-spacing: 1.5px; text-transform: uppercase; }
  .person-title { font-size: 13px; margin-top: 2px; }
  .rule { border-top: 1px dotted var(--panel-text); opacity: .7; margin: 14px 0; }
  .company-lines { font-size: 12.5px; line-height: 1.5; }
  .contact-list { list-style: none; font-size: 13px; }
  .contact-list li { display: flex; align-items: center; gap: 12px; line-height: 1.75; }
  .contact-list svg { width: 12px; height: 12px; flex: none; fill: var(--panel-text); }
</style>
</head>
<body>
<main class="stage">
  <section class="card card--back" aria-label="Card back">
    <p class="back-name">Brantwell Group</p>
    <p class="back-web">www.brantwellgroup.example</p>
  </section>

  <section class="card card--front" aria-label="Card front">
    <div class="front-brand">
      <span class="brand-mark"></span>
      <p class="brand-name">Brantwell<br>Group</p>
    </div>
    <div class="front-details">
      <p class="person-name">Peter J. Haldane</p>
      <p class="person-title">President</p>
      <div class="rule"></div>
      <p class="company-lines">Brantwell Group LLC<br>Finance and Strategy Consulting<br>Aviation - Manufacturing - Energy</p>
      <div class="rule"></div>
      <ul class="contact-list">
        <li>
          <svg viewBox="0 0 24 24" aria-hidden="true"><path d="M6.6 10.8a15.1 15.1 0 0 0 6.6 6.6l2.2-2.2a1 1 0 0 1 1-.25 11.4 11.4 0 0 0 3.6.57 1 1 0 0 1 1 1V20a1 1 0 0 1-1 1A17 17 0 0 1 3 4a1 1 0 0 1 1-1h3.5a1 1 0 0 1 1 1c0 1.25.2 2.45.57 3.57a1 1 0 0 1-.25 1z"/></svg>
          (555) 304-6198
        </li>
        <li>
          <svg viewBox="0 0 24 24" aria-hidden="true"><path d="M2 5h20v14H2z M4 7l8 6 8-6" fill="none" stroke="#e6eef8" stroke-width="2"/></svg>
          ph@brantwellgroup.example
        </li>
        <li>
          <svg viewBox="0 0 24 24" aria-hidden="true"><circle cx="12" cy="12" r="10" fill="none" stroke="#e6eef8" stroke-width="2"/><path d="M2 12h20M12 2c3 3 3 17 0 20M12 2c-3 3-3 17 0 20" fill="none" stroke="#e6eef8" stroke-width="1.5"/></svg>
          brantwellgroup.example
        </li>
      </ul>
    </div>
  </section>
</main>
</body>
</html>
```